Legal Consultant: Book cover for "Silver Ridge Transitions" in Australia.

This project is for the desiign of the front cover of a book t be published in perfect bond (A5) and as an eBook.

The target readers are Australian law firm partners.

I am a lawyer and senior legal recruitment consultant specialisng in the recruitment of law firm partners. I have written a short book that advises law firm partners how to make a lateral move to another law firm. It's simply about recruitment at a senior level. The book sets out the steps to maximise the partner's opportunity to engage the services of a senior legal recruitment consultant and then identify suitable law firms, interview techniques and preparation. A key element in the book is the preparation of various documents to submit to potential law firms eg CV, business plan, financial performance.

I know the eBook design has to 'grab" the reader so the title will need to jump out at the reader.

Target Market(s)

Senior law firm partners in Australia

Industry/Entity Type

Graphic Design

Requirements
Must have
• The cover must also be suitable for eBook publication. Therefore it must stand out from competitive publications.
Nice to have
• A design suitable for senior professional services executves.
Should not have
• No cliches eg shaking hands, two men in suits, judge's gavel etc

```html
<!DOCTYPE html>
<html lang="en">
<head>
<meta charset="UTF-8">
<title>A Partner's Guide: Planning Your Next Chapter — Book Cover</title>
<link href="https://fonts.googleapis.com/css2?family=Alegreya+Sans:wght@300;400&display=swap" rel="stylesheet">
<style>
  :root {
    --backdrop: #d9d9d9;
    --cover-ground: #221314;
    --type-light: #f4efea;
    --spine-dark: #3a2218;
    --spine-mid: #7a5233;
    --spine-gold: #a67a4a;
    --spine-plum: #4e2a2c;
    --spine-rose: #8a4a3e;
  }
  * { margin: 0; padding: 0; box-sizing: border-box; }
  html, body {
    width: 1200px;
    height: 900px;
    overflow: hidden;
    background: var(--backdrop);
  }
  .canvas {
    position: relative;
    width: 1200px;
    height: 900px;
  }
  .book-cover {
    position: absolute;
    left: 297px;
    top: 20px;
    width: 606px;
    height: 860px;
    background: var(--cover-ground);
    overflow: hidden;
    font-family: "Alegreya Sans", sans-serif;
    color: var(--type-light);
  }
  .spine-stack {
    position: absolute;
    left: 0;
    top: 0;
    width: 318px;
    height: 100%;
    background: linear-gradient(
      180deg,
      var(--spine-mid) 0%,
      var(--spine-gold) 10%,
      var(--spine-mid) 16%,
      var(--spine-plum) 24%,
      var(--spine-gold) 34%,
      var(--spine-mid) 46%,
      var(--spine-gold) 58%,
      var(--spine-plum) 72%,
      var(--spine-rose) 84%,
      var(--spine-mid) 94%,
      var(--spine-dark) 100%
    );
  }
  .series-label {
    position: absolute;
    right: 24px;
    top: 96px;
    font-size: 28px;
    font-weight: 400;
    letter-spacing: 0.2px;
  }
  .book-title {
    position: absolute;
    right: 24px;
    top: 516px;
    text-align: right;
    font-size: 56px;
    font-weight: 300;
    line-height: 70px;
    letter-spacing: 0.3px;
    white-space: nowrap;
  }
  .author-credit {
    position: absolute;
    right: 24px;
    top: 686px;
    font-size: 17px;
    font-weight: 400;
    letter-spacing: 0.2px;
    white-space: nowrap;
  }
</style>
</head>
<body>
  <main class="canvas">
    <section class="book-cover">
      <div class="spine-stack" role="img" aria-label="Stack of antique leather-bound books with gilded spines"></div>
      <p class="series-label">A PARTNER'S GUIDE:</p>
      <h1 class="book-title">PLANNING YOUR<br>NEXT CHAPTER</h1>
      <p class="author-credit">DANIEL HARTLEY LL.B BARRISTER-AT-LAW</p>
    </section>
  </main>
</body>
</html>
```